Nonna's Granary - Flour Bag Packing for Fit and Healthy Flour

Nonna's Granary is a family owned company that was incorporated in honor of our grandfather who is in the pic below. We would like to incorporate that picture into the packaging design. We would also like for the logo to represent a modern/fit lifestyle that is unique from the current competition.

Nonna's flour is a newly practiced style of milling that allows for flour to be consumed in its natural/organic state. We don't not bleach, chemically treat or add any enriched/preservative additives to our flour. This allows for freshness (our priority) and the natural flavors of the nutty grain to seep into our flour.

Our flour contains all the nutritional value that comes from all the components of Wheat Family Grains.

Our Family has been in the flour business for 60+ years and we established our mill in Debar Macedonia in 1998.

100% Organic
Non GMO
Family Owned
Stone Milled
Banner (Product Types): All Purpose Flour, Whole Wheat Flour, Pastry Flour, Artisan (Bread) Flour
Size: 1 KG / 5 KG / 25 KG

Flour is good for: Cookies, Cakes, Bread, Biscuits, Brownies, Muffins, Pastries, Pancakes, Rolls, Pizza Crust Pies

Target Market(s)

Fit Lifestyle, Hipsters, Modern, NYC

Industry/Entity Type

Agtech

Logo Text

Nonna's Granary

Requirements
Must have
• Nonna's Pic must be incorporated somehow on the bag. He will provide a friendly face and a homier feeling. The pic does not need to be the Center Piece. The logo will be the Center Piece.
Nice to have
• Nonna's Granary on the side of the bags or some cool/hip design.

```html
<!DOCTYPE html>
<html lang="en">
<head>
<meta charset="utf-8">
<title>Nonna's Flour – Bag Front</title>
<link href="https://fonts.googleapis.com/css2?family=Open+Sans:wght@600;700;800&family=PT+Sans+Narrow:wght@700&display=swap" rel="stylesheet">
<style>
  :root {
    --backdrop-light: #f6f6f6;
    --backdrop-dark: #e4e4e4;
    --kraft: #c7a07a;
    --kraft-dark: #b48c66;
    --orange: #d4621c;
    --orange-dark: #b94e10;
    --brown: #3b2a20;
    --brown-text: #3a2a1f;
    --white: #ffffff;
    --badge-ring: #a58f84;
    --gold: #b89a5c;
    --portrait-tone: #9c7a5c;
  }
  html, body {
    margin: 0;
    padding: 0;
    width: 1200px;
    height: 1200px;
    overflow: hidden;
  }
  body {
    background: radial-gradient(circle at 50% 40%, var(--backdrop-light), var(--backdrop-dark));
    font-family: "Open Sans", Arial, sans-serif;
    position: relative;
  }
  .bag-front {
    position: absolute;
    left: 168px;
    top: 180px;
    width: 540px;
    height: 870px;
    background: linear-gradient(180deg, var(--kraft) 0%, var(--kraft-dark) 100%);
    overflow: hidden;
    box-shadow: 0 6px 18px rgba(0,0,0,0.15);
  }
  .band {
    position: absolute;
    left: 0;
    width: 100%;
    background: linear-gradient(180deg, var(--orange) 0%, var(--orange-dark) 100%);
  }
  .band--top { top: 78px; height: 102px; }
  .band--bottom { top: 780px; height: 72px; }
  .portrait-area {
    position: absolute;
    left: 330px;
    top: 230px;
    width: 240px;
    height: 520px;
    border-radius: 50% 40% 30% 45%;
    background: radial-gradient(ellipse at 50% 40%, rgba(156,122,92,0.55), rgba(156,122,92,0) 70%);
  }
  .bag-badge {
    position: absolute;
    left: 186px;
    top: 30px;
    width: 168px;
    height: 168px;
    border-radius: 50%;
    background: var(--white);
    border: 6px solid var(--badge-ring);
    box-sizing: border-box;
    display: flex;
    align-items: center;
    justify-content: center;
    text-align: center;
  }
  .bag-badge__name {
    font-weight: 800;
    font-size: 22px;
    line-height: 1.15;
    color: var(--brown);
  }
  .product-name {
    position: absolute;
    left: 0;
    width: 100%;
    text-align: center;
    color: var(--white);
    font-weight: 800;
    text-shadow: 3px 3px 0 rgba(70,45,25,0.45);
    margin: 0;
  }
  .product-name--brand { top: 185px; font-size: 104px; letter-spacing: 1px; line-height: 1; }
  .product-name--type { top: 383px; font-size: 64px; line-height: 1; }
  .rule {
    position: absolute;
    left: 54px;
    width: 402px;
    height: 4px;
    background: var(--white);
    box-shadow: 2px 2px 0 rgba(70,45,25,0.35);
  }
  .rule--upper { top: 372px; }
  .rule--lower { top: 518px; }
  .ribbon {
    position: absolute;
    left: 124px;
    top: 454px;
    width: 264px;
    height: 52px;
  }
  .ribbon__label {
    position: absolute;
    inset: 0;
    display: flex;
    align-items: center;
    justify-content: center;
    color: var(--white);
    font-weight: 600;
    font-size: 26px;
  }
  .claims {
    position: absolute;
    top: 540px;
    left: 0;
    width: 100%;
    display: flex;
    justify-content: center;
    gap: 22px;
    margin: 0;
    padding: 0;
    list-style: none;
    font-family: "PT Sans Narrow", "Arial Narrow", sans-serif;
    font-weight: 700;
    font-size: 22px;
    color: var(--brown-text);
  }
  .claims li::before {
    content: "";
    display: inline-block;
    width: 7px;
    height: 7px;
    border-radius: 50%;
    background: var(--orange);
    margin-right: 4px;
    vertical-align: middle;
  }
  .flour-type {
    position: absolute;
    left: 106px;
    top: 588px;
    width: 300px;
    height: 104px;
  }
  .flour-type__label {
    position: absolute;
    inset: 0;
    display: flex;
    flex-direction: column;
    align-items: center;
    justify-content: center;
    color: var(--white);
    font-weight: 700;
    font-size: 25px;
    line-height: 1.1;
  }
  .uses {
    position: absolute;
    left: 40px;
    top: 706px;
    width: 440px;
    margin: 0;
    font-family: "PT Sans Narrow", "Arial Narrow", sans-serif;
    font-weight: 700;
    font-size: 17px;
    line-height: 1.4;
    color: var(--brown-text);
    text-align: center;
    font-weight: 400;
  }
  .weight {
    position: absolute;
    left: 222px;
    top: 780px;
    width: 72px;
    height: 72px;
    border-radius: 50%;
    background: var(--white);
    display: flex;
    align-items: center;
    justify-content: center;
    font-weight: 800;
    font-size: 19px;
    color: var(--brown);
  }
  .brand-badge {
    position: absolute;
    left: 756px;
    top: 76px;
    width: 444px;
    height: 444px;
    border-radius: 50%;
    background: var(--white);
    display: flex;
    align-items: center;
    justify-content: center;
    text-align: center;
  }
  .brand-badge__name {
    font-weight: 800;
    font-size: 54px;
    line-height: 1.15;
    color: var(--gold);
  }
</style>
</head>
<body>
  <main class="bag-front">
    <div class="band band--top"></div>
    <div class="band band--bottom"></div>

    <div class="portrait-area" role="img" aria-label="Faint photo of the family grandfather"></div>

    <div class="bag-badge">
      <span class="bag-badge__name">Nonna's<br>Granary</span>
    </div>

    <h1 class="product-name product-name--brand">NONNA’S</h1>
    <div class="rule rule--upper"></div>
    <h2 class="product-name product-name--type">FLOUR</h2>

    <div class="ribbon">
      <svg width="264" height="52" viewBox="0 0 264 52" aria-hidden="true">
        <polygon points="0,10 24,10 24,46 0,46 10,28" fill="var(--orange-dark)"/>
        <polygon points="264,10 240,10 240,46 264,46 254,28" fill="var(--orange-dark)"/>
        <rect x="16" y="4" width="232" height="38" fill="var(--orange)"/>
      </svg>
      <span class="ribbon__label">100% ORGANIC</span>
    </div>
    <div class="rule rule--lower"></div>

    <ul class="claims">
      <li>Non GMO</li>
      <li>Family Owned</li>
      <li>Stone Milled</li>
    </ul>

    <div class="flour-type">
      <svg width="300" height="104" viewBox="0 0 300 104" aria-hidden="true">
        <polygon points="14,52 34,6 266,6 286,52 266,98 34,98" fill="var(--orange)"/>
        <polygon points="22,52 40,12 260,12 278,52 260,92 40,92" fill="var(--brown)"/>
      </svg>
      <div class="flour-type__label"><span>ALL PURPOSE</span><span>FLOUR</span></div>
    </div>

    <p class="uses">Flour is good for: Cookies, Cakes, Bread, Biscuits, Brownies, Muffins, Pastries, Pancakes, Rolls, Pizza Crust Pies</p>

    <div class="weight">1 KG</div>
  </main>

  <aside class="brand-badge">
    <span class="brand-badge__name">Nonna's<br>Granary</span>
  </aside>
</body>
</html>
```